parts and kits

we need an updated flyer to email to our customers
we need to have what we sell at kivo
caliper pistons
seal kits
new brake cylinders
brake boosters
brake shoes
brake pads
brake hoses
cables -accelerator, clutch, hand brake etc
for both private, vintage and commercial vehicles

```html
<!DOCTYPE html>
<html lang="en">
<head>
<meta charset="utf-8">
<title>Kivo Auto Centre – Parts and Kits</title>
<link rel="stylesheet" href="https://fonts.googleapis.com/css2?family=Archivo+Black&family=Fjalla+One&display=swap">
<style>
  :root {
    --yellow: #ecdc4a;
    --black: #000000;
    --white: #ffffff;
    --navy: #141a4a;
    --steel-light: #e9eaea;
    --steel-mid: #b9b8b4;
    --steel-dark: #6f6b63;
    --blue-light: #cfe0ea;
    --blue-mid: #5f87a6;
    --blue-deep: #2a4f70;
    --charcoal: #2a2a2a;
    --charcoal-light: #4a4a4a;
    --part-grey: #9a9a9a;
  }
  * { margin: 0; padding: 0; box-sizing: border-box; }
  html, body { width: 927px; height: 1200px; overflow: hidden; background: var(--white); }
  .flyer {
    position: relative;
    width: 927px;
    height: 1200px;
    overflow: hidden;
    font-family: "Fjalla One", "Arial Narrow", sans-serif;
  }
  .hero-photo {
    position: absolute; left: 0; top: 0; width: 927px; height: 364px;
    background: linear-gradient(100deg, var(--steel-dark) 0%, var(--steel-mid) 35%, var(--steel-light) 65%, var(--white) 100%);
  }
  .brand-name {
    position: absolute; left: 0; width: 927px; text-align: center;
    font-family: "Archivo Black", "Arial Black", sans-serif;
    color: var(--yellow); line-height: 1;
  }
  .brand-name--main { top: 12px; font-size: 262px; letter-spacing: -6px; padding-right: 60px; }
  .brand-name--sub { top: 222px; font-size: 132px; letter-spacing: -3px; padding-left: 0; }
  .specialist-band {
    position: absolute; left: 0; top: 364px; width: 927px; height: 100px;
    background: var(--black); color: var(--white); text-align: center;
  }
  .specialist-band__tagline { position: absolute; top: 10px; left: 0; width: 927px; font-size: 22px; padding-left: 0; }
  .specialist-band__headline { position: absolute; top: 43px; left: 0; width: 927px; font-size: 39px; line-height: 1.2; }
  .workshop-photo {
    position: absolute; left: 0; top: 464px; width: 927px; height: 579px;
    background: linear-gradient(180deg, var(--blue-light) 0%, var(--blue-mid) 20%, var(--blue-deep) 60%, var(--blue-mid) 100%);
  }
  .vehicle-types {
    position: absolute; left: 0; top: 470px; width: 927px; text-align: center;
    font-size: 31px; color: var(--navy); line-height: 1.2;
  }
  .product-list {
    position: absolute; left: 37px; top: 553px; list-style: none;
    color: var(--white); font-size: 30px; line-height: 43.9px;
  }
  .part-callouts { position: absolute; left: 0; top: 0; width: 927px; height: 1200px; }
  .aim-band {
    position: absolute; left: 0; top: 1043px; width: 927px; height: 157px;
    background: radial-gradient(ellipse at 50% 40%, var(--charcoal-light) 0%, var(--charcoal) 70%);
    border-top: 3px solid var(--white);
    color: var(--yellow); text-align: center;
  }
  .aim-band__title { position: absolute; top: 30px; left: 0; width: 927px; font-size: 44px; line-height: 1.2; }
  .aim-band__rule { position: absolute; top: 60px; height: 4px; background: var(--white); opacity: .85; }
  .aim-band__rule--left { left: 275px; width: 85px; }
  .aim-band__rule--right { left: 578px; width: 86px; }
  .aim-band__text { position: absolute; top: 79px; left: 0; width: 927px; font-size: 27px; line-height: 1.2; }
</style>
</head>
<body>
<main class="flyer">
  <div class="hero-photo" role="img" aria-label="Close-up photograph of brake shoes, caliper and a brake disc"></div>
  <h1>
    <span class="brand-name brand-name--main">KIVO</span>
    <span class="brand-name brand-name--sub">Auto Centre</span>
  </h1>

  <section class="specialist-band">
    <p class="specialist-band__tagline">The Brake and Cable Specialists</p>
    <p class="specialist-band__headline">Specialise in the Re- Manufacture of Brakes,Hoses</p>
  </section>

  <div class="workshop-photo" role="img" aria-label="Photograph of a mechanic's hands fitting a brake disc in a workshop"></div>
  <p class="vehicle-types">Parts for motorbikes ,cars,commercial etc</p>

  <ul class="product-list">
    <li>caliper pistons</li>
    <li>seal kits</li>
    <li>new brake cylinders</li>
    <li>brake boosters</li>
    <li>brake shoes</li>
    <li>brake pads</li>
    <li>brake hoses</li>
    <li>cables -accelerator,</li>
    <li>clutch, hand brake etc</li>
    <li>for both private, vintage</li>
  </ul>

  <svg class="part-callouts" viewBox="0 0 927 1200" aria-hidden="false">
    <g class="callout">
      <rect x="549" y="580" width="192" height="57" fill="var(--yellow)" stroke="var(--black)" stroke-width="1.5"/>
      <circle cx="477" cy="607" r="83" fill="var(--white)" stroke="var(--yellow)" stroke-width="11"/>
      <circle cx="477" cy="607" r="88.5" fill="none" stroke="var(--black)" stroke-width="1.5"/>
      <circle cx="477" cy="607" r="77" fill="var(--part-grey)" role="img" aria-label="Photograph of a pair of brake pads"/>
    </g>
    <g class="callout">
      <rect x="637" y="738" width="173" height="55" fill="var(--yellow)" stroke="var(--black)" stroke-width="1.5"/>
      <circle cx="560" cy="771" r="83" fill="var(--white)" stroke="var(--yellow)" stroke-width="11"/>
      <circle cx="560" cy="771" r="88.5" fill="none" stroke="var(--black)" stroke-width="1.5"/>
      <circle cx="560" cy="771" r="77" fill="#a8a8a6" role="img" aria-label="Photograph of a drilled brake disc with caliper"/>
    </g>
    <g class="callout">
      <rect x="560" y="902" width="177" height="58" fill="var(--yellow)" stroke="var(--black)" stroke-width="1.5"/>
      <circle cx="478" cy="928" r="81" fill="var(--white)" stroke="var(--yellow)" stroke-width="11"/>
      <circle cx="478" cy="928" r="86.5" fill="none" stroke="var(--black)" stroke-width="1.5"/>
      <circle cx="478" cy="928" r="75" fill="#b4b4b4" role="img" aria-label="Photograph of a chrome brake booster"/>
    </g>
  </svg>

  <section class="aim-band">
    <span class="aim-band__rule aim-band__rule--left"></span>
    <h2 class="aim-band__title">Our aim is</h2>
    <span class="aim-band__rule aim-band__rule--right"></span>
    <p class="aim-band__text">to repair parts with the quickest turn -around times possible</p>
  </section>
</main>
</body>
</html>
```